Non-profit sports organization needs templates for Word and InDesign

"Fralo Teens" is a non-profit organization in Winterthur, which supports the recruitment of young talent by the handball clubs in Winterthur. Every year we run several camps, a tournament for schoolchildren and several handball lessons at school.
During these activities there are always written information. So far we have not given much thought to the design. But since we think that a professional design will also lead to more interaction, we now turn to you as a designer.

For the communication with partners, sponsors, patrons, etc. we need a uniform appearance. Since different departments are currently working with different programs, we need a template for letters and documentation for Word and InDesign.

We will need the documentation template for project descriptions, information, etc.
The letter templates are needed to contact sponsors, authorities, patrons, etc.

Both the letter template and the documentation template should look modern. The design should be based on the existing flyers. Otherwise we have no other requirements so far.

Homepage: www.fralo-teens.ch

Target Market(s)

Letters, documentation or information to authorities, sponsors, associations, patrons, members, participants, etc.

Requirements
Must have
• In addition to the design, the templates should also contain a concept for titles, paragraphs, lists, etc. (colors / fonts / ...)

Word and Indesign templates

```html
<!DOCTYPE html>
<html lang="en">
<head>
<meta charset="utf-8">
<title>Fralo Teens – Letterhead</title>
<link rel="stylesheet" href="https://fonts.googleapis.com/css2?family=Montserrat:wght@400;500;700&display=swap">
<style>
  :root {
    --brand-red: #e11f1d;
    --brand-red-dark: #c8141a;
    --brand-blue: #1b5fd8;
    --header-grey: #e6e8e9;
    --text-grey: #8c8c8c;
    --paper: #ffffff;
  }
  * { margin: 0; padding: 0; box-sizing: border-box; }
  html, body { width: 857px; height: 1200px; overflow: hidden; background: var(--paper); }
  body { font-family: "Montserrat", Arial, sans-serif; color: var(--text-grey); }

  .letterhead { position: relative; width: 857px; height: 1200px; overflow: hidden; background: var(--paper); }

  .header-shape { position: absolute; left: 0; top: 0; }

  .brand {
    position: absolute; left: 80px; top: 62px;
    display: flex; align-items: center; gap: 12px;
  }
  .brand-dot { width: 30px; height: 30px; border-radius: 50%; background: var(--brand-red); }
  .brand-name { font-weight: 700; font-size: 30px; color: var(--brand-red); letter-spacing: 0.5px; }

  .header-url {
    position: absolute; right: 42px; top: 98px;
    font-weight: 700; font-size: 20px; color: var(--paper); letter-spacing: 0.3px;
  }

  .content { position: absolute; left: 74px; top: 262px; width: 720px; }
  .headline {
    font-weight: 700; font-size: 39px; color: var(--brand-red);
    letter-spacing: 0.3px; margin-bottom: 16px;
  }
  .subhead {
    font-weight: 700; font-size: 23px; color: var(--brand-red);
    margin-top: 36px; margin-bottom: 6px;
  }
  .body-text {
    font-size: 14.6px; line-height: 26.4px; white-space: nowrap;
    margin-bottom: 26px;
  }

  .signature { position: absolute; left: 600px; top: 912px; font-size: 15.5px; line-height: 24px; }
  .signature .closing { margin-bottom: 52px; }

  .footer-shape { position: absolute; left: 0; top: 1106px; }
  .footer-url {
    position: absolute; left: 0; right: 0; top: 1148px; text-align: center;
    font-weight: 700; font-size: 20px; color: var(--paper); letter-spacing: 0.3px;
  }
</style>
</head>
<body>
<div class="letterhead">

  <svg class="header-shape" width="857" height="170" viewBox="0 0 857 170" aria-hidden="true">
    <path d="M0 0 H857 V86 H560 C470 86 420 110 395 150 C300 160 120 158 0 154 Z" fill="var(--header-grey)"/>
    <path d="M402 136 C440 104 490 88 570 86 H857 V136 Z" fill="var(--brand-blue)"/>
    <path d="M0 154 C150 160 330 162 402 136 L405 138 C330 166 150 164 0 158 Z" fill="var(--paper)"/>
  </svg>

  <div class="brand">
    <span class="brand-dot"></span>
    <span class="brand-name">Fralo Teens</span>
  </div>
  <div class="header-url">www.fralo-teens.ch</div>

  <main class="content">
    <h1 class="headline">YOUR HEADLINE</h1>
    <p class="body-text">Duis autem vel eum iriure dolor in hendrerit in vulputate velit esse molestie con-<br>sequat, vel illum dolore eu feugiat nulla facilisis at vero eros et accumsan et iusto odio<br>dignissim qui blandit praesent luptatum zzril delenit augue duis dolore te feugait<br>nulla facilisi.</p>
    <p class="body-text">Lorem ipsum dolor sit amet, cons ectetuer adipiscing elit, sed diam nonummy nibh<br>euismod tincidunt ut laoreet dolore magna aliquam erat volutpat.</p>

    <h2 class="subhead">YOUR TEXT HERE</h2>
    <p class="body-text">Lorem ipsum dolor sit amet, consectetuer adipiscing elit, sed diam nonummy nibh<br>euismod tincidunt ut laoreet dolore magna aliquam erat volutpat. Ut wisi enim ad<br>minim veniam, quis nostrud exerci tation ullamcorper suscipit lobortis nisl ut aliquip<br>ex ea commodo consequat. Duis autem vel eum iriure dolor in hendrerit in vulputa-<br>te velit esse molestie consequat, vel illum dolore eu feugiat nulla facilisis at vero eros<br>et accumsan et iusto odio dignissim qui blandit praesent luptatum zzril delenit<br>augue duis dolore te feugait nulla facilisi.</p>
    <p class="body-text">Vel illum dolore eu feugiat nulla facilisis at vero eros et accumsan et iusto odio dig-<br>nissim qui blandit praesent luptatum zzril delenit augue duis dolore te feugait nulla<br>facilisi.</p>
  </main>

  <div class="signature">
    <p class="closing">Regard</p>
    <p>Marlene<br>Art Director</p>
  </div>

  <svg class="footer-shape" width="857" height="94" viewBox="0 0 857 94" aria-hidden="true">
    <path d="M0 4 H796 Q806 4 806 14 V22 H0 Z" fill="var(--brand-blue)"/>
    <defs>
      <linearGradient id="footerRed" x1="0" y1="0" x2="1" y2="0">
        <stop offset="0" stop-color="var(--brand-red)"/>
        <stop offset="1" stop-color="var(--brand-red-dark)"/>
      </linearGradient>
    </defs>
    <rect x="0" y="27" width="857" height="67" fill="url(#footerRed)"/>
  </svg>
  <div class="footer-url">www.fralo-teens.ch</div>

</div>
</body>
</html>
```